Digipack-Design für Blues Trio aus Berlin gesucht
Zielgruppe
Wie sind ein Blues Trio aus Berlin mit eigenen Songs. Im März ist das erste Album fertig und wir brauchen ein ansprechendes Cover.
Geplant ist ein Digipack. Für dieses Projekt brauchen wir eine schöne Vorderseite.
Name der Band: Kardel Folk
Aufgabenstellung
Keine Gewaltbilder, Sex, Alkohol, Knochen, usw. Wir sind keine Metalband =)
Wenn möglich freundliche, warme Farben verwenden.
Wir haben ein paar Cover angehangen, die zeigen was wir schön finden. Vielleicht hilft das.
Auf unserer Seite KardelFolk-musik.de findet man noch das ein oder andere Bild, falls das gebraucht wird.
Bitte KEINE Blues-Klischees bedienen!

```html
<!DOCTYPE html>
<html lang="de">
<head>
<meta charset="utf-8">
<title>Kardel Folk – The Album</title>
<link rel="stylesheet" href="https://fonts.googleapis.com/css2?family=Heebo:wght@100;300&display=swap">
<style>
  :root {
    --sky-top: #80cbd1;
    --sky-bottom: #9de8ea;
    --wall: #3b3f39;
    --band-blue: #00ade8;
    --band-grey: #a4a5a2;
    --text-white: #ffffff;
  }
  html, body {
    margin: 0;
    padding: 0;
    width: 1200px;
    height: 1197px;
    overflow: hidden;
    background: var(--wall);
  }
  .cover {
    position: relative;
    width: 1200px;
    height: 1197px;
    overflow: hidden;
  }
  .cover-photo {
    position: absolute;
    inset: 0;
    background: linear-gradient(to bottom,
      var(--sky-top) 0%,
      var(--sky-bottom) 62%,
      var(--wall) 78%,
      var(--wall) 100%);
  }
  .accent-bands {
    position: absolute;
    inset: 0;
  }
  .band-name {
    position: absolute;
    top: 585px;
    left: 0;
    width: 1200px;
    margin: 0;
    text-align: center;
    font-family: "Heebo", sans-serif;
    font-weight: 100;
    font-size: 86px;
    line-height: 1;
    letter-spacing: 2px;
    color: var(--text-white);
  }
  .album-title {
    position: absolute;
    top: 1000px;
    margin: 0;
    font-family: "Heebo", sans-serif;
    font-weight: 100;
    font-size: 128px;
    line-height: 1;
    color: var(--text-white);
  }
  .album-title--the { left: 318px; }
  .album-title--album { left: 652px; }
</style>
</head>
<body>
  <main class="cover">
    <div class="cover-photo" role="img" aria-label="Foto: Flachdach eines modernen Gebäudes mit weißer Stütze vor hellem türkisfarbenem Himmel"></div>

    <svg class="accent-bands" width="1200" height="1197" viewBox="0 0 1200 1197" aria-hidden="true">
      <polygon class="band band--left" points="0,822 544,691 544,765 0,898" fill="var(--band-blue)"/>
      <polygon class="band band--right" points="623,780 1200,910 1200,982 623,853" fill="var(--band-blue)"/>
      <polygon class="band band--grey" points="0,946 271,1000 271,1079 0,1026" fill="var(--band-grey)"/>
    </svg>

    <h1 class="band-name">KARDEL FOLK</h1>

    <h2 class="album-title album-title--the">THE</h2>
    <h2 class="album-title album-title--album">ALBUM</h2>
  </main>
</body>
</html>
```